LA Billboard Project for Brisk Lending

We are running three different billboards around LA, and we need someone to take the mock-ups I've created and bring this campaign to life. Whatever wording is on the mock-ups should stay the same in the ads you create, but feel free to get creative with layout and style. I've attached our mock-ups, our style guide, our logo, and the necessary specs for the billboards. If you have any questions, feel free to reach out!

```html
<!DOCTYPE html>
<html lang="en">
<head>
<meta charset="utf-8">
<title>Brisk Lending – LA Billboards</title>
<link rel="stylesheet" href="https://fonts.googleapis.com/css2?family=Barlow+Condensed:wght@700&family=Montserrat:wght@800&family=Nunito+Sans:wght@400;600;800&display=swap">
<style>
  :root {
    --navy: #13254a;
    --block: #3e3f5c;
    --yellow: #f2de2a;
    --cyan: #2ec4d6;
    --white: #ffffff;
    --page: #ffffff;
  }
  * { margin: 0; padding: 0; box-sizing: border-box; }
  html, body { width: 774px; height: 1200px; overflow: hidden; background: var(--page); }
  .canvas { position: relative; width: 774px; height: 1200px; }

  .billboard {
    position: absolute;
    left: 46px;
    width: 684px;
    height: 314px;
    background: var(--navy);
    overflow: hidden;
    box-shadow: 0 10px 18px rgba(0,0,0,0.28);
  }
  .billboard--refi { top: 56px; }
  .billboard--apply { top: 443px; }
  .billboard--pride { top: 835px; }

  .billboard__art { position: absolute; inset: 0; width: 100%; height: 100%; }

  .headline {
    position: absolute;
    font-family: "Barlow Condensed", "Arial Narrow", sans-serif;
    font-weight: 700;
    color: var(--yellow);
    line-height: 1;
    white-space: nowrap;
    letter-spacing: 1px;
  }
  .lead {
    position: absolute;
    font-family: "Nunito Sans", "Avenir", sans-serif;
    font-weight: 400;
    color: var(--white);
    line-height: 1;
    white-space: nowrap;
  }
  .body-line {
    position: absolute;
    font-family: "Nunito Sans", sans-serif;
    font-weight: 600;
    font-size: 22px;
    color: var(--white);
    line-height: 1;
    white-space: nowrap;
    transform: translateY(-50%);
  }
  .body-line .stat {
    font-family: "Barlow Condensed", sans-serif;
    font-weight: 700;
    font-size: 28px;
    color: var(--yellow);
    margin: 0 4px;
  }
  .brand-name {
    position: absolute;
    left: 524px;
    transform: translate(-50%, -50%);
    font-family: "Nunito Sans", sans-serif;
    font-weight: 800;
    font-size: 30px;
    color: var(--cyan);
    white-space: nowrap;
    line-height: 1;
  }
  .web-address {
    position: absolute;
    transform: translateY(-50%);
    font-family: "Montserrat", sans-serif;
    font-weight: 800;
    font-size: 19px;
    letter-spacing: 3px;
    color: var(--navy);
    line-height: 1;
    white-space: nowrap;
  }
  .web-address--long {
    font-size: 15px;
    letter-spacing: 1px;
  }
</style>
</head>
<body>
<main class="canvas">

  <svg width="0" height="0" style="position:absolute">
    <defs>
      <linearGradient id="photo-keys" x1="0" y1="0" x2="1" y2="1">
        <stop offset="0" stop-color="#f1ece8"/>
        <stop offset="0.45" stop-color="#e2c2ae"/>
        <stop offset="1" stop-color="#d9d7d4"/>
      </linearGradient>
      <linearGradient id="photo-traffic" x1="0" y1="0" x2="1" y2="1">
        <stop offset="0" stop-color="#9aa1a6"/>
        <stop offset="0.5" stop-color="#5e6368"/>
        <stop offset="1" stop-color="#a4a6a6"/>
      </linearGradient>
      <linearGradient id="photo-flag" x1="0" y1="0" x2="1" y2="1">
        <stop offset="0" stop-color="#7dc2f2"/>
        <stop offset="0.5" stop-color="#b4dcf7"/>
        <stop offset="1" stop-color="#e3f1fb"/>
      </linearGradient>
      <g id="frame">
        <rect x="920" y="0" width="193" height="152" fill="var(--block)"/>
        <rect x="1191" y="0" width="161" height="152" fill="var(--block)"/>
        <rect x="920" y="229" width="193" height="191" fill="var(--block)"/>
        <rect x="1191" y="229" width="161" height="191" fill="var(--block)"/>
        <polygon points="0,62 185,0 205,0 0,80" fill="var(--yellow)"/>
        <polygon points="0,400 108,620 82,620 0,452" fill="var(--yellow)"/>
        <polygon points="0,520 667,520 513,585 0,585" fill="var(--yellow)"/>
        <path d="M560 0 L745 410 Q770 470 715 500 L430 620" fill="none" stroke="var(--cyan)" stroke-width="12"/>
      </g>
    </defs>
  </svg>

  <!-- Billboard 1 -->
  <section class="billboard billboard--refi">
    <svg class="billboard__art" viewBox="0 0 1352 620" preserveAspectRatio="none">
      <path role="img" aria-label="Photo of a hand holding a key with a small wooden house keyring" d="M0 0 H560 L745 410 Q770 470 715 500 L430 620 H0 Z" fill="url(#photo-keys)"/>
      <use href="#frame"/>
    </svg>
    <div class="lead" style="left:370px; top:48px; font-size:31px;">What’s Your</div>
    <div class="headline" style="left:358px; top:84px; font-size:52px;">MORTGAGE</div>
    <div class="headline" style="left:420px; top:133px; font-size:54px;">STRATEGY?</div>
    <div class="brand-name" style="top:253px;">Brisk Lending</div>
    <div class="web-address" style="left:63px; top:280px;">BRISKREFI.COM</div>
  </section>

  <!-- Billboard 2 -->
  <section class="billboard billboard--apply">
    <svg class="billboard__art" viewBox="0 0 1352 620" preserveAspectRatio="none">
      <path role="img" aria-label="Photo of cars queued in heavy traffic" d="M0 0 H560 L745 410 Q770 470 715 500 L430 620 H0 Z" fill="url(#photo-traffic)"/>
      <use href="#frame"/>
    </svg>
    <div class="headline" style="left:349px; top:25px; font-size:54px;">TRAFFIC IS</div>
    <div class="headline" style="left:455px; top:78px; font-size:54px;">A MESS.</div>
    <div class="lead" style="left:392px; top:138px; font-size:27px;">Your Mortgage</div>
    <div class="lead" style="left:392px; top:171px; font-size:27px;">doesn’t have to be.</div>
    <div class="brand-name" style="top:250px;">Brisk Lending</div>
    <div class="web-address" style="left:50px; top:283px;">BRISKAPPLY.COM</div>
  </section>

  <!-- Billboard 3 -->
  <section class="billboard billboard--pride">
    <svg class="billboard__art" viewBox="0 0 1352 620" preserveAspectRatio="none">
      <path role="img" aria-label="Photo of a rainbow pride flag waving against a blue sky" d="M0 0 H560 L745 410 Q770 470 715 500 L430 620 H0 Z" fill="url(#photo-flag)"/>
      <use href="#frame"/>
    </svg>
    <div class="headline" style="left:392px; top:28px; font-size:37px;">DID YOU KNOW</div>
    <div class="body-line" style="left:367px; top:86px;">that Same-Sex Borrowers</div>
    <div class="body-line" style="left:378px; top:119px;">are<span class="stat">73%</span>more likely to be</div>
    <div class="body-line" style="left:391px; top:152px;">denied when aplying</div>
    <div class="body-line" style="left:414px; top:185px;">for a morgage loan?</div>
    <div class="brand-name" style="top:248px;">Brisk Lending</div>
    <div class="web-address web-address--long" style="left:14px; top:281px;">BRISKLENDING.COM/LGBTQ</div>
  </section>

</main>
</body>
</html>
```